Design for a real estate wev portal

Contents and features of the site
---------------------------------
Website in 5 languages: French, Dutch, English, German, Spanish.
English name of the site: Lantern Nest Place
Main purpose of the site:
- allow people to rent their house/ appartment for flatsharing purposes.
- help people wanting to find a room in flatsharing
- help people to find additional roommates for their flatsharing
Key interaction sequence:
1. I create a "group" of people who have common interest/hobbies
2. People who have the same interests/hobbies join my group
3. I look for a house/appartment to host my group
Website structure will be the following:
- Home
- Groups
-- Look for a group
--- Join a group
-- Create a group
- Properties
-- Look for a house/appartement
-- Apply
- Sales conditions
- Contact
- My account
-- My profile
-- My groups OR my properties
Your mission
------------
The client has no graphical guidelines, simply a logo (see attached).
We need a (responsive compliant) design for the following pages (we expect PSD's from you. No HTML nor CSS):
1. homepage (see example and wireframe attached)
2. properties search result list (see wireframe attached)
3. "detailed" form for properties
4. groups search result list
5. "detailed" form for groups
6. my account page
FOR THE COMPETITION step we only expect from you the design of first 2 screens.
Based on that, we will select the designer who will win the project, and will have to design the 4 remaining screens.
Target Market(s)
B2C
Industry/Entity Type
Real Estate
Number of Pages Required
5+ page
Look and feel
Each slider illustrates characteristics of the customer's brand and the style your logo design should communicate.

```html
<!DOCTYPE html>
<html lang="en">
<head>
<meta charset="utf-8">
<title>Lantern Nest Place – Search result</title>
<link href="https://fonts.googleapis.com/css2?family=Lato:wght@400;700&display=swap" rel="stylesheet">
<style>
:root{
  --green:#5cb83c;
  --green-dark:#3f8f22;
  --green-soft:#d9f5cc;
  --teal:#1f6f86;
  --text:#333b40;
  --muted:#7a858c;
  --line:#dde2e6;
  --page:#f0f4f9;
  --band:#e8eef6;
  --blue:#1aa3e6;
  --orange:#f08a1c;
  --foot:#1b2525;
  --foot-deep:#151d1d;
}
*{box-sizing:border-box;margin:0;padding:0}
html,body{width:903px;height:1200px;overflow:hidden}
body{font-family:"Lato",sans-serif;color:var(--text);background:var(--page);position:relative;font-size:7px}
.site-header{position:absolute;left:0;top:0;width:903px;height:52px;background:#fff;border-bottom:1px solid var(--line)}
.main-nav{position:absolute;left:176px;top:22px;display:flex;align-items:center;gap:12px;font-size:6.5px;font-weight:700;letter-spacing:.1px}
.main-nav a{color:var(--text);text-decoration:none;position:relative}
.main-nav a.active{color:var(--green)}
.main-nav a.active::after{content:"";position:absolute;left:0;right:-10px;top:18px;height:2px;background:var(--green)}
.caret{font-size:5px;margin-left:3px;color:var(--muted)}
.brand{position:absolute;left:407px;top:16px;display:flex;align-items:center;gap:5px;font-size:11px;font-weight:700;color:var(--teal)}
.brand .dot{width:8px;height:8px;border-radius:50%;background:var(--green)}
.account-nav{position:absolute;right:176px;top:22px;display:flex;gap:12px;font-size:6.5px;font-weight:700}
.crumbs{position:absolute;left:0;top:52px;width:903px;height:18px;background:var(--band);padding:6px 177px;font-size:5px;color:var(--text)}
.crumbs .home{color:var(--green)}
.sidebar{position:absolute;left:176px;top:81px;width:127px}
.search-box{height:28px;background:var(--green);color:#e6f6dd;font-size:6px;padding:11px 10px;position:relative}
.search-box svg{position:absolute;right:9px;top:9px}
.filters{background:#fff;padding:12px 11px 6px}
.f-label{font-size:6px;margin-bottom:7px;display:flex;justify-content:space-between}
.range{height:2px;background:var(--line);position:relative;margin:0 0 17px}
.range .fill{position:absolute;left:0;top:0;width:67%;height:2px;background:var(--green)}
.range .knob{position:absolute;left:63%;top:-4px;width:10px;height:10px;border-radius:50%;background:var(--green)}
.row{display:flex;gap:7px;margin-bottom:13px}
.field{flex:1;height:20px;border:1px solid var(--line);font-size:6px;padding:6px 6px;display:flex;justify-content:space-between}
.field.ph{color:#b8c0c5}
.seg{display:flex;margin-bottom:13px}
.seg span{flex:1;height:20px;border:1px solid var(--line);font-size:6px;display:flex;align-items:center;justify-content:center;gap:4px}
.seg span+span{border-left:none}
.seg span.on{background:var(--green-soft);border-color:var(--green);color:var(--green)}
.check{display:flex;align-items:center;gap:6px;font-size:6px;margin-bottom:5px}
.check i{width:10px;height:10px;border:1px solid var(--line);display:flex;align-items:center;justify-content:center}
.check i.on{border-color:var(--green)}
.checks{margin:16px 0 15px}
.results{position:absolute;left:317px;top:81px;width:410px}
.res-head{height:22px;display:flex;align-items:center;justify-content:space-between;font-size:6px;margin-bottom:7px}
.sort{display:flex;align-items:center;gap:5px}
.sort .sel{width:90px;height:21px;background:#fff;padding:7px 7px;display:flex;justify-content:space-between;font-size:6px}
.card{height:92px;background:#fff;display:flex;margin-bottom:9px;position:relative;box-shadow:0 1px 2px rgba(0,0,0,.04)}
.photo{width:134px;height:92px;flex:none}
.info{padding:10px 15px;flex:1}
.info h3{font-size:8px;font-weight:400;color:var(--teal);margin-bottom:4px}
.meta{display:flex;align-items:center;gap:5px;font-size:5.8px;margin-bottom:4px}
.badge{display:inline-block;background:var(--blue);color:#fff;font-size:4.5px;font-weight:700;padding:2px 3px;margin-bottom:6px}
.desc{font-size:5.8px;line-height:9px;color:var(--text)}
.desc b{font-size:4.8px;margin-left:2px}
.fav{position:absolute;right:12px;top:11px}
.pager{position:absolute;left:317px;top:932px;width:410px;height:30px;background:#fff;display:flex;align-items:center;padding:0 10px;font-size:6px;justify-content:space-between}
.pages{display:flex;gap:11px;margin-left:60px}
.pages span.cur{color:var(--green);border-bottom:1.5px solid var(--green);padding-bottom:6px;margin-bottom:-7px}
.site-footer{position:absolute;left:0;top:1025px;width:903px;height:143px;background:var(--foot);color:#c7d0d0}
.f-title{position:absolute;font-size:7px;letter-spacing:.2px}
.f-title::after{content:"";display:block;width:35px;height:1px;background:var(--green);margin-top:13px}
.f-title.plain::after{display:none}
.f-links{position:absolute;font-size:6px;color:#8c9898;line-height:14px}
.pre-search{position:absolute;left:176px;top:54px;display:flex;height:25px}
.pre-search .kw{width:88px;background:#253030;color:#5d6a6a;font-size:6px;padding:9px 8px}
.pre-search .cat{width:83px;background:#253030;margin-left:1px;font-size:6px;padding:9px 8px;display:flex;justify-content:space-between;color:#c7d0d0}
.pre-search .go{width:54px;margin-left:4px;background:var(--green-dark);color:#0e2608;font-size:6.5px;font-weight:700;display:flex;align-items:center;justify-content:center}
.copyright{position:absolute;left:0;top:1168px;width:903px;height:32px;background:var(--foot-deep);color:#4f5b5b;font-size:5px;text-align:center;padding-top:14px}
</style>
</head>
<body>
<header class="site-header">
  <nav class="main-nav">
    <svg width="8" height="8" viewBox="0 0 10 10"><path d="M5 1 1 5h1.3v4h2.2V6.5h1V9h2.2V5H9z" fill="#333b40"/></svg>
    <a href="#">GROUP<span class="caret">&#9660;</span></a>
    <a href="#" class="active">PROPERTIES<span class="caret">&#9660;</span></a>
    <a href="#">SALES CONDITIONS</a>
  </nav>
  <div class="brand"><span class="dot"></span>Lantern Nest Place</div>
  <nav class="account-nav"><span>LOGIN</span><span>REGISTER</span></nav>
</header>
<div class="crumbs"><span class="home">HOME</span> &gt; SEARCH RESULT</div>

<aside class="sidebar">
  <div class="search-box">Type keywords here ...
    <svg width="10" height="10" viewBox="0 0 10 10"><circle cx="4.2" cy="4.2" r="3" fill="none" stroke="#fff" stroke-width="1.1"/><path d="M6.5 6.5 9 9" stroke="#fff" stroke-width="1.2"/></svg>
  </div>
  <div class="filters">
    <div class="f-label"><span>Location range</span><span>20 km</span></div>
    <div class="range"><div class="fill"></div><div class="knob"></div></div>
    <div class="f-label"><span>Price range (€)</span></div>
    <div class="row"><div class="field ph">Min</div><div class="field">5,000</div></div>
    <div class="f-label"><span>Type of house</span></div>
    <div class="seg"><span>House</span><span class="on">Apartment</span></div>
    <div class="f-label"><span>Rooms</span></div>
    <div class="seg"><span>1</span><span class="on">2</span><span>3</span><span>4</span></div>
    <div class="checks">
      <div class="check"><i class="on"><svg width="7" height="6" viewBox="0 0 7 6"><path d="M.7 3 2.7 5 6.3.8" fill="none" stroke="#5cb83c" stroke-width="1.1"/></svg></i>Listing with photo</div>
      <div class="check"><i class="on"><svg width="7" height="6" viewBox="0 0 7 6"><path d="M.7 3 2.7 5 6.3.8" fill="none" stroke="#5cb83c" stroke-width="1.1"/></svg></i>Double bedrooms</div>
      <div class="check"><i></i>Furniture</div>
      <div class="check"><i></i>Short duration</div>
    </div>
    <div class="f-label"><span>Age of roommates</span></div>
    <div class="row"><div class="field">35<span>&#8964;</span></div><div class="field">40<span>&#8964;</span></div></div>
    <div class="f-label"><span>Roommates gender</span></div>
    <div class="seg"><span class="on">Male</span><span>Female</span></div>
    <div class="f-label"><span>Roommate status</span></div>
    <div class="seg"><span class="on">Student</span><span>Employee</span></div>
  </div>
</aside>

<main class="results">
  <div class="res-head"><span>1,638 properties found</span><div class="sort">Sort : <div class="sel"><span>Recent added</span><span>&#8964;</span></div></div></div>

  <article class="card"><div class="photo" role="img" aria-label="Bright bedroom with large window" style="background:linear-gradient(135deg,#8a7f75,#d8d2cb 60%,#6a6560)"></div>
    <div class="info"><h3>Nice House of Lorem Ipsum</h3>
      <div class="meta"><svg width="6" height="8" viewBox="0 0 6 8"><path d="M3 0a3 3 0 0 0-3 3c0 2 3 5 3 5s3-3 3-5a3 3 0 0 0-3-3z" fill="#9aa3a8"/></svg>London</div>
      <div class="meta"><svg width="7" height="7" viewBox="0 0 7 7"><path d="M3.5 0 0 3h1v4h5V3h1z" fill="#5cb83c"/></svg>Rent per month</div>
      <span class="badge">AVAILABILITY</span>
      <p class="desc">Lorem ipsum dolor sit amet, consectetur adipiscing elit, sed do eiusmod tempor incididunt ut labore et dolore magna aliqua. Ut enim ad minim veniam, ... <b>VIEW DETAILS</b></p></div>
    <svg class="fav" width="14" height="15" viewBox="0 0 14 15"><circle cx="7" cy="7" r="6" fill="none" stroke="#9aa3a8" stroke-width="1.6"/><path d="M7 4l.9 1.9 2 .2-1.5 1.3.5 2L7 8.4 5.1 9.4l.5-2L4.1 6.1l2-.2z" fill="#9aa3a8"/></svg>
  </article>

  <article class="card"><div class="photo" role="img" aria-label="Modern kitchen with dark cabinets" style="background:linear-gradient(135deg,#e8e4df,#5a4a40 55%,#c9c2ba)"></div>
    <div class="info"><h3>Small Apartment of Lorem Ipsum</h3>
      <div class="meta"><svg width="6" height="8" viewBox="0 0 6 8"><path d="M3 0a3 3 0 0 0-3 3c0 2 3 5 3 5s3-3 3-5a3 3 0 0 0-3-3z" fill="#9aa3a8"/></svg>Brussels</div>
      <div class="meta"><svg width="7" height="7" viewBox="0 0 7 7"><path d="M3.5 0 0 3h1v4h5V3h1z" fill="#5cb83c"/></svg>Rent per month</div>
      <span class="badge">AVAILABILITY</span>
      <p class="desc">Lorem ipsum dolor sit amet, consectetur adipiscing elit, sed do eiusmod tempor incididunt ut labore et dolore magna aliqua. Ut enim ad minim veniam, ... <b>VIEW DETAILS</b></p></div>
    <svg class="fav" width="14" height="15" viewBox="0 0 14 15"><circle cx="7" cy="7" r="6" fill="none" stroke="#f08a1c" stroke-width="1.6"/><path d="M7 4l.9 1.9 2 .2-1.5 1.3.5 2L7 8.4 5.1 9.4l.5-2L4.1 6.1l2-.2z" fill="#f08a1c"/></svg>
  </article>

  <article class="card"><div class="photo" role="img" aria-label="Living room with sofa and patterned rug" style="background:linear-gradient(135deg,#cfd8dc,#b9a88f 55%,#2f2f33)"></div>
    <div class="info"><h3>Wonderfull Penthouse of Lorem Ipsum</h3>
      <div class="meta"><svg width="6" height="8" viewBox="0 0 6 8"><path d="M3 0a3 3 0 0 0-3 3c0 2 3 5 3 5s3-3 3-5a3 3 0 0 0-3-3z" fill="#9aa3a8"/></svg>Brussels</div>
      <div class="meta"><svg width="7" height="7" viewBox="0 0 7 7"><path d="M3.5 0 0 3h1v4h5V3h1z" fill="#5cb83c"/></svg>Rent per month</div>
      <span class="badge">AVAILABILITY</span>
      <p class="desc">Lorem ipsum dolor sit amet, consectetur adipiscing elit, sed do eiusmod tempor incididunt ut labore et dolore magna aliqua. Ut enim ad minim veniam, ... <b>VIEW DETAILS</b></p></div>
    <svg class="fav" width="14" height="15" viewBox="0 0 14 15"><circle cx="7" cy="7" r="6" fill="none" stroke="#f08a1c" stroke-width="1.6"/><path d="M7 4l.9 1.9 2 .2-1.5 1.3.5 2L7 8.4 5.1 9.4l.5-2L4.1 6.1l2-.2z" fill="#f08a1c"/></svg>
  </article>

  <article class="card"><div class="photo" role="img" aria-label="Sunlit lounge with fireplace" style="background:linear-gradient(135deg,#9c8c78,#e6e2dc 50%,#7a6e62)"></div>
    <div class="info"><h3>House of Lorem Ipsum</h3>
      <div class="meta"><svg width="6" height="8" viewBox="0 0 6 8"><path d="M3 0a3 3 0 0 0-3 3c0 2 3 5 3 5s3-3 3-5a3 3 0 0 0-3-3z" fill="#9aa3a8"/></svg>London</div>
      <div class="meta"><svg width="7" height="7" viewBox="0 0 7 7"><path d="M3.5 0 0 3h1v4h5V3h1z" fill="#5cb83c"/></svg>Rent per month</div>
      <span class="badge">AVAILABILITY</span>
      <p class="desc">Lorem ipsum dolor sit amet, consectetur adipiscing elit, sed do eiusmod tempor incididunt ut labore et dolore magna aliqua. Ut enim ad minim veniam, ... <b>VIEW DETAILS</b></p></div>
    <svg class="fav" width="14" height="15" viewBox="0 0 14 15"><circle cx="7" cy="7" r="6" fill="none" stroke="#9aa3a8" stroke-width="1.6"/><path d="M7 4l.9 1.9 2 .2-1.5 1.3.5 2L7 8.4 5.1 9.4l.5-2L4.1 6.1l2-.2z" fill="#9aa3a8"/></svg>
  </article>

  <article class="card"><div class="photo" role="img" aria-label="Cosy living room with framed pictures" style="background:linear-gradient(135deg,#d9d3cc,#a89d92 55%,#ece7e1)"></div>
    <div class="info"><h3>The House of Lorem Ipsum</h3>
      <div class="meta"><svg width="6" height="8" viewBox="0 0 6 8"><path d="M3 0a3 3 0 0 0-3 3c0 2 3 5 3 5s3-3 3-5a3 3 0 0 0-3-3z" fill="#9aa3a8"/></svg>London</div>
      <div class="meta"><svg width="7" height="7" viewBox="0 0 7 7"><path d="M3.5 0 0 3h1v4h5V3h1z" fill="#5cb83c"/></svg>Rent per month</div>
      <span class="badge">AVAILABILITY</span>
      <p class="desc">Lorem ipsum dolor sit amet, consectetur adipiscing elit, sed do eiusmod tempor incididunt ut labore et dolore magna aliqua. Ut enim ad minim veniam, ... <b>VIEW DETAILS</b></p></div>
    <svg class="fav" width="14" height="15" viewBox="0 0 14 15"><circle cx="7" cy="7" r="6" fill="none" stroke="#9aa3a8" stroke-width="1.6"/><path d="M7 4l.9 1.9 2 .2-1.5 1.3.5 2L7 8.4 5.1 9.4l.5-2L4.1 6.1l2-.2z" fill="#9aa3a8"/></svg>
  </article>

  <article class="card"><div class="photo" role="img" aria-label="Elegant bedroom with chandelier" style="background:linear-gradient(135deg,#4a4a4c,#e4e2e0 50%,#b7b0a8)"></div>
    <div class="info"><h3>The Wonderfull Penthouse of Lorem Ipsum</h3>
      <div class="meta"><svg width="6" height="8" viewBox="0 0 6 8"><path d="M3 0a3 3 0 0 0-3 3c0 2 3 5 3 5s3-3 3-5a3 3 0 0 0-3-3z" fill="#9aa3a8"/></svg>Brussels</div>
      <div class="meta"><svg width="7" height="7" viewBox="0 0 7 7"><path d="M3.5 0 0 3h1v4h5V3h1z" fill="#5cb83c"/></svg>Rent per month</div>
      <span class="badge">AVAILABILITY</span>
      <p class="desc">Lorem ipsum dolor sit amet, consectetur adipiscing elit, sed do eiusmod tempor incididunt ut labore et dolore magna aliqua. Ut enim ad minim veniam, ... <b>VIEW DETAILS</b></p></div>
    <svg class="fav" width="14" height="15" viewBox="0 0 14 15"><circle cx="7" cy="7" r="6" fill="none" stroke="#f08a1c" stroke-width="1.6"/><path d="M7 4l.9 1.9 2 .2-1.5 1.3.5 2L7 8.4 5.1 9.4l.5-2L4.1 6.1l2-.2z" fill="#f08a1c"/></svg>
  </article>

  <article class="card"><div class="photo" role="img" aria-label="Bedroom with turquoise wall" style="background:linear-gradient(135deg,#2d8c9a,#3e3430 55%,#d7d0c6)"></div>
    <div class="info"><h3>House of Lorem Ipsum</h3>
      <div class="meta"><svg width="6" height="8" viewBox="0 0 6 8"><path d="M3 0a3 3 0 0 0-3 3c0 2 3 5 3 5s3-3 3-5a3 3 0 0 0-3-3z" fill="#9aa3a8"/></svg>London</div>
      <div class="meta"><svg width="7" height="7" viewBox="0 0 7 7"><path d="M3.5 0 0 3h1v4h5V3h1z" fill="#5cb83c"/></svg>Rent per month</div>
      <span class="badge">AVAILABILITY</span>
      <p class="desc">Lorem ipsum dolor sit amet, consectetur adipiscing elit, sed do eiusmod tempor incididunt ut labore et dolore magna aliqua. Ut enim ad minim veniam, ... <b>VIEW DETAILS</b></p></div>
    <svg class="fav" width="14" height="15" viewBox="0 0 14 15"><circle cx="7" cy="7" r="6" fill="none" stroke="#9aa3a8" stroke-width="1.6"/><path d="M7 4l.9 1.9 2 .2-1.5 1.3.5 2L7 8.4 5.1 9.4l.5-2L4.1 6.1l2-.2z" fill="#9aa3a8"/></svg>
  </article>

  <article class="card"><div class="photo" role="img" aria-label="Living room opening onto a garden view" style="background:linear-gradient(135deg,#6b7f95,#cbbfa9 50%,#5f7d6a)"></div>
    <div class="info"><h3>The House of the house of Lorem Ipsum</h3>
      <div class="meta"><svg width="6" height="8" viewBox="0 0 6 8"><path d="M3 0a3 3 0 0 0-3 3c0 2 3 5 3 5s3-3 3-5a3 3 0 0 0-3-3z" fill="#9aa3a8"/></svg>London</div>
      <div class="meta"><svg width="7" height="7" viewBox="0 0 7 7"><path d="M3.5 0 0 3h1v4h5V3h1z" fill="#5cb83c"/></svg>Rent per month</div>
      <span class="badge">AVAILABILITY</span>
      <p class="desc">Lorem ipsum dolor sit amet, consectetur adipiscing elit, sed do eiusmod tempor incididunt ut labore et dolore magna aliqua. Ut enim ad minim veniam, ... <b>VIEW DETAILS</b></p></div>
    <svg class="fav" width="14" height="15" viewBox="0 0 14 15"><circle cx="7" cy="7" r="6" fill="none" stroke="#9aa3a8" stroke-width="1.6"/><path d="M7 4l.9 1.9 2 .2-1.5 1.3.5 2L7 8.4 5.1 9.4l.5-2L4.1 6.1l2-.2z" fill="#9aa3a8"/></svg>
  </article>
</main>

<nav class="pager">
  <span>&lsaquo;&nbsp;&nbsp;&nbsp;Previous</span>
  <div class="pages"><span>1</span><span>2</span><span class="cur">3</span><span>4</span><span>5</span><span>6</span><span>...</span><span>25</span></div>
  <span style="margin-left:auto">Next&nbsp;&nbsp;&nbsp;&rsaquo;</span>
</nav>

<footer class="site-footer">
  <div class="f-title plain" style="left:176px;top:37px">PRE-DEFINED SEARCH</div>
  <div class="pre-search"><div class="kw">Keyword is here ...</div><div class="cat"><span>Accomodation</span><span>&#8964;</span></div><div class="go">SEARCH</div></div>
  <div class="f-title" style="left:452px;top:37px">QUICK LINKS</div>
  <div class="f-links" style="left:452px;top:69px">Home<br>Sales Conditions<br>Contact</div>
  <div class="f-title" style="left:539px;top:37px">GROUPS</div>
  <div class="f-links" style="left:539px;top:69px">Look for a group<br>Create a group</div>
  <div class="f-title" style="left:633px;top:37px">PROPERTIES</div>
  <div class="f-links" style="left:633px;top:69px">Look for a house/apartment<br>Apply</div>
</footer>
<div class="copyright">Copyright 2016 LANTERN NEST PLACE. All rights reserved.</div>
</body>
</html>
```